Business school needs a web design

Who We are:
IZPM is a small business school that offers programs in Project Management. The school is based in West Africa and welcomes students from the whole area. Our aim is to become one of the reference business schools in Africa.

Project Brief:
The site will include all informations relevant for different types of visitors that we have: actual and future students, companies, mass media, future employees, ect. It will present information about subscription, list of programs, presentation of the school and its team,etc.

What We want:
This competition is for Design only no coding! We need design for two pages.
We did some wireframing for the home page and the list of programs page. We made them just to show how we imagine the website would look like. But we encourage creative designs, so you don't have to stick to the wireframe models.

Sites We like:
http://www.larchmontgate.example/
http://www.pelvarin.example/fr/etudes.html
http://www.qwd.example/mba/Pages/default.aspx

Color schemes
The logo of the school is red and black. So the color scheme of the website should match that. For the rest, it is opened to your imagination.
Updates

The payment for the project is now garanteed. Good luck to you all !

Target Market(s)

The target market is diversified because we have students of different ages, also company representatives or employees that might visit the website for recruitment purposes. But the majority of our audience should be aged between 20 - 30 years.

Industry/Entity Type

Small Business

Requirements
Must have
• The design must include two pages: a home page and another interior page : might be the list of programs or any other page relevant to the domain. The Home page must include a slide show at the beginning.
The background page must be white.
Nice to have
• The use of flat design for this project is preferred.
The use of Chirply bootstrap as a base for the design is an asset.

```html
<!DOCTYPE html>
<html lang="fr">
<head>
<meta charset="utf-8">
<title>IZPM – Accueil</title>
<link href="https://fonts.googleapis.com/css2?family=Ubuntu:wght@400;500;700&family=Roboto:wght@400;500;700&family=Noto+Serif&display=swap" rel="stylesheet">
<style>
:root{
  --red:#c4161c;
  --red-dark:#b10e12;
  --ink:#333;
  --muted:#6a6a6a;
  --bar:#3b3b3b;
  --line:#dcdcdc;
  --paper:#fff;
  --bg:#ededed;
}
*{box-sizing:border-box;margin:0;padding:0}
html,body{width:960px;height:1200px;overflow:hidden}
body{font-family:Roboto,Arial,sans-serif;color:var(--ink);background:var(--bg)}
.page{position:relative;width:960px;height:1200px;overflow:hidden;background:linear-gradient(#e4e4e4,#f4f4f4 300px,#f4f4f4)}
.abs{position:absolute}
a{color:inherit;text-decoration:none}

.topbar{left:0;top:0;width:960px;height:18px;background:var(--bar);border-bottom:2px solid var(--red)}
.topbar nav{position:absolute;right:151px;top:3px;font-size:9px;color:#fff;letter-spacing:.2px}
.topbar nav span{margin:0 4px;color:#bbb}

.sheet{left:138px;top:18px;width:685px;height:1012px;background:var(--paper)}

.brand{left:151px;top:38px;display:flex;align-items:center;gap:6px;font-family:Ubuntu,sans-serif;font-weight:700;font-size:30px;color:var(--red)}
.brand i{display:block;width:14px;height:14px;background:var(--red)}

.phone{left:685px;top:42px;font-size:13px;color:#444;display:flex;align-items:center;gap:6px}
.search{left:688px;top:63px;width:121px;height:20px;border:1px solid #ccc;border-radius:3px;font-size:9px;font-style:italic;color:#777;padding:4px 9px}
.search svg{position:absolute;right:5px;top:4px}

.mainnav{left:151px;top:98px;width:658px;height:29px;background:linear-gradient(#555,#333);border-radius:4px;display:flex;box-shadow:0 2px 2px rgba(0,0,0,.25)}
.mainnav a{font-family:Ubuntu,sans-serif;font-weight:500;font-size:11.5px;color:#fff;display:flex;align-items:center;justify-content:center;border-right:1px solid #222;box-shadow:1px 0 0 #666}
.mainnav a:last-child{border:0;box-shadow:none}

.slider{left:151px;top:138px;width:658px;height:247px;background:#e2e2e2;border:1px solid #d4d4d4}
.slide{left:4px;top:4px;width:650px;height:238px;background:linear-gradient(110deg,#5e6d3c 0%,#7f9552 35%,#8c8a6e 60%,#6f7f43 100%)}
.caption{left:14px;top:94px;font-family:'Noto Serif',serif;font-size:26px;line-height:30px;color:#fff;text-shadow:0 1px 3px rgba(0,0,0,.5)}
.dots{left:263px;top:212px;width:138px;height:26px;background:#e2e2e2;border-radius:14px 14px 0 0;display:flex;justify-content:center;align-items:center;gap:6px}
.dots i{width:14px;height:14px;border-radius:50%;background:#fff;border:2px solid #ccc}
.dots i.on{background:var(--red);border-color:#fff}

.sec{font-family:Ubuntu,sans-serif;font-size:14.5px;color:var(--red);display:flex;align-items:center;gap:8px;white-space:nowrap}
.sec::before,.sec::after{content:"";height:5px;border-top:1px solid var(--line);border-bottom:1px solid var(--line);flex:1}
.sec::before{flex:0 0 20px}
.sec .mark{width:10px;height:10px;border-radius:50%;background:var(--red);flex:0 0 10px}

.video{left:163px;top:448px;width:192px;height:125px;background:linear-gradient(#c9ccd0,#9da2aa)}
.video .ctrl{position:absolute;left:0;bottom:0;width:100%;height:12px;background:#1f2a3a}
.play{left:80px;top:42px}
.intro{left:370px;top:448px;width:204px;font-size:10px;line-height:14px;letter-spacing:.6px;color:#666}
.intro a{display:inline-block;margin-top:3px;color:#222;text-decoration:underline;letter-spacing:0}

.tabs{left:163px;top:597px;width:412px;height:21px;border-bottom:2px solid var(--red);display:flex;font-family:Ubuntu,sans-serif;font-size:10px;color:#555}
.tabs span{padding:4px 6px 0}
.tabs .on{background:var(--red);color:#fff;font-weight:500;padding:4px 4px 0}
.links{font-size:8.5px;line-height:20px;color:#333;list-style:none}
.photo-class{left:438px;top:631px;width:137px;height:72px;background:linear-gradient(#eef0f2,#c7ccd2)}

.event-date{width:30px;height:31px;border:1px solid #999;border-radius:2px;text-align:center;font-size:9.5px;line-height:14px;background:#fff}
.event-date b{display:block;background:#666;color:#fff;font-weight:400}
.event-date em{font-style:normal;color:var(--red);font-weight:700;background:#eee;display:block}
.item-title{font-size:8px;font-weight:500;color:#333}
.item-text{font-size:8.5px;line-height:12px;letter-spacing:.5px;color:#666}
.blogimg{width:70px;height:60px;border:2px solid #e1e1e1;background:linear-gradient(#c7d1d7,#a7a08a)}
.blog .date{font-size:8.5px;color:var(--red);font-weight:700}
.blog .t{font-size:8.5px;font-weight:700}
.blog .x{font-size:8.5px;line-height:11px;color:#666}
.blog .m{font-size:8.5px;text-decoration:underline;color:#333}
.more{font-size:8.5px;font-weight:500;color:#222}
.more b{color:var(--red)}
.hr{height:1px;background:var(--line)}
.dotted{height:0;border-top:1px dotted #bbb}

.vdiv{left:589px;top:412px;width:1px;height:490px;background:var(--line)}
.audience{left:602px;top:448px;font-size:12px;line-height:18.6px;color:#444;list-style:none}
.audience li::before{content:"";display:inline-block;border-left:6px solid #333;border-top:4px solid transparent;border-bottom:4px solid transparent;margin-right:10px}
.newsimg{width:46px;height:45px;background:linear-gradient(135deg,#e6c24a,#7e5d34)}
.newstext{width:148px;font-size:9.5px;line-height:12px;letter-spacing:.6px;color:#666}

.partners-line{left:163px;top:918px;width:608px;height:6px;border-top:1px solid var(--line);border-bottom:3px solid #e5e5e5}
.partner{top:946px;font-family:Ubuntu,sans-serif;font-weight:700;font-size:22px;color:#37538c;transform:translateX(-50%)}

.footer{left:0;top:1030px;width:960px;height:170px;background:var(--red-dark);color:#fff;border-top:2px solid #8c0a0d}
.fcol{top:16px}
.fcol h4{font-family:Ubuntu,sans-serif;font-weight:500;font-size:13px;padding-bottom:6px;border-bottom:1px dotted rgba(255,255,255,.5);min-width:90px;display:inline-block;white-space:nowrap;margin-bottom:10px}
.fcol ul{display:block}
.fcol li{list-style:none;font-size:8.8px;line-height:17.5px}
.social li{display:flex;align-items:center;gap:8px;line-height:21px}
.social i{width:16px;height:16px;border-radius:50%;background:#fff;display:block}
.fcol p{font-size:8.8px;line-height:11px}
.news-in{display:flex;margin-top:10px;width:110px;height:17px;border-radius:9px;background:#fff;overflow:hidden}
.news-in span{flex:1;border-right:1px solid #bbb}
.news-in b{font-size:8px;color:#444;padding:3px 6px}
.copy{left:0;top:148px;width:960px;text-align:center;font-size:9.5px}

.sidebar{left:925px;top:466px;width:35px;height:166px;background:#3b3b3b;border-radius:5px 0 0 5px;display:flex;flex-direction:column;align-items:center;justify-content:space-evenly}
.sidebar i{display:block;width:18px;height:18px;border-radius:50%;background:#fff}
</style>
</head>
<body>
<div class="page">

  <header class="topbar abs">
    <nav>Repertoire du personel<span>|</span>Blogue<span>|</span>Solle de presse<span>|</span>Nous joindre<span>|</span>Francais</nav>
  </header>

  <div class="sheet abs"></div>

  <div class="brand abs"><i></i>IZPM</div>

  <div class="phone abs">
    <svg width="13" height="13" viewBox="0 0 24 24"><path fill="#c4161c" d="M6.6 10.8a15 15 0 0 0 6.6 6.6l2.2-2.2c.3-.3.7-.4 1-.2 1.1.4 2.3.6 3.6.6.6 0 1 .4 1 1V20c0 .6-.4 1-1 1A17 17 0 0 1 3 4c0-.6.4-1 1-1h3.5c.6 0 1 .4 1 1 0 1.3.2 2.5.6 3.6.1.3 0 .7-.2 1z"/></svg>
    (221) 33 412 77 90
  </div>
  <div class="search abs">Search
    <svg width="11" height="11" viewBox="0 0 24 24"><circle cx="10" cy="10" r="6.5" fill="none" stroke="#888" stroke-width="2.5"/><path d="M15 15l6 6" stroke="#888" stroke-width="3"/></svg>
  </div>

  <nav class="mainnav abs">
    <a style="width:134px">A Propos de l'izpm</a>
    <a style="width:178px">Programmes et Formations</a>
    <a style="width:84px">Etudiants</a>
    <a style="width:170px">Nouvelles et Evenements</a>
    <a style="width:92px">Enterprises</a>
  </nav>

  <section class="slider abs">
    <div class="slide abs" role="img" aria-label="Photo d'un groupe d'étudiants assis sur une pelouse de campus">
      <h1 class="caption abs" style="font-weight:400">Lorem ipsum dolor sit<br>amet, consectetuer<br>adipiscing elit.</h1>
    </div>
    <div class="dots abs"><i class="on"></i><i></i><i></i><i></i></div>
  </section>

  <h2 class="sec abs" style="left:163px;top:409px;width:412px;font-weight:500">Devenez Les Gestionnaires De Demain</h2>

  <div class="video abs" role="img" aria-label="Vidéo : réunion de formation en salle">
    <div class="ctrl"></div>
    <svg class="play abs" width="30" height="36" viewBox="0 0 30 36"><path d="M2 2l26 16L2 34z" fill="rgba(60,60,60,.7)"/></svg>
  </div>
  <div class="intro abs">Lorem ipsum dolor sit amet, consectetuer adipiscing elit, sed diam nonummy nibh euismod tincidunt ut laoreet dolore magna aliquam erat volutpat. Ut wisi enim ad minim veniam, quis nostrud exerci tation ullamcorper suscipit lobortis nisl ut aliquip ex ea commodo consequat. Duis autem vel eum iriure dolor in hendrerit...<br><a>read more</a></div>

  <div class="tabs abs">
    <span class="on">Prospective students</span><span>Current Students</span><span>Alumni &amp; friends</span><span>Parents</span><span>Faculty &amp; Staff</span>
  </div>
  <ul class="links abs" style="left:165px;top:627px">
    <li>&gt; View programs</li><li>&gt; Ask a Question</li><li>&gt; International student info</li><li>&gt; Continuing education</li>
  </ul>
  <ul class="links abs" style="left:304px;top:627px">
    <li>&gt; Undergraduate programs</li><li>&gt; Graduate programs</li><li>&gt; Co-operative education</li><li>&gt; Find out more</li>
  </ul>
  <div class="photo-class abs" role="img" aria-label="Photo d'une formatrice devant une classe"></div>

  <h2 class="sec abs" style="left:163px;top:719px;width:196px;font-weight:500">Evenements</h2>
  <h2 class="sec abs" style="left:369px;top:719px;width:206px;font-weight:500">Blouge</h2>

  <div class="event-date abs" style="left:163px;top:758px"><b>JAN</b><em>07</em></div>
  <div class="abs" style="left:207px;top:756px;width:146px">
    <div class="item-title">Lorem Ipsum dummy</div>
    <div class="item-text">Lorem ipsum dolor sit amet, consectetuer adipiscing elit, sed diam nonummy nibh euism</div>
  </div>
  <div class="hr abs" style="left:165px;top:821px;width:192px"></div>
  <div class="event-date abs" style="left:163px;top:832px"><b>JAN</b><em>07</em></div>
  <div class="abs" style="left:207px;top:831px;width:146px">
    <div class="item-title">Lorem Ipsum dummy</div>
    <div class="item-text">Lorem ipsum dolor sit amet, consectetuer adipiscing elit, sed diam nonummy nibh euism</div>
  </div>
  <div class="more abs" style="left:165px;top:885px">Tous les evenements <b>&gt;&gt;</b></div>

  <div class="blogimg abs" style="left:369px;top:750px" role="img" aria-label="Photo d'une étudiante en train d'écrire"></div>
  <div class="blog abs" style="left:449px;top:750px;width:126px">
    <div class="date">Jan 03, 2014</div><div class="t">Title</div>
    <div class="x">Lorem ipsum dolor sit am nibh euismod...</div><div class="m">Lira la suite</div>
  </div>
  <div class="dotted abs" style="left:369px;top:821px;width:206px"></div>
  <div class="blogimg abs" style="left:369px;top:834px" role="img" aria-label="Photo d'une étudiante en train d'écrire"></div>
  <div class="blog abs" style="left:450px;top:835px;width:126px">
    <div class="date">Jan 03, 2014</div><div class="t">Title</div>
    <div class="x">Lorem ipsum dolor sit am nibh euismod...</div><div class="m">Lira la suite</div>
  </div>
  <div class="abs" style="left:369px;top:900px;width:206px;height:3px;background:#e0e0e0"></div>

  <div class="vdiv abs"></div>
  <h2 class="sec abs" style="left:602px;top:409px;width:207px;font-weight:500">Vous etes<span class="mark"></span></h2>
  <ul class="audience abs">
    <li>Futur etudiant</li><li>Etudiant actuel</li><li>Entreprise</li><li>Employeur</li><li>Postulant</li><li>Medias</li><li>Partenaires</li>
  </ul>
  <h2 class="sec abs" style="left:602px;top:590px;width:207px;font-weight:500">Nouvelles<span class="mark"></span></h2>

  <div class="newsimg abs" style="left:602px;top:636px" role="img" aria-label="Photo d'actualité : étudiante au travail"></div>
  <div class="newstext abs" style="left:657px;top:635px">Lorem ipsum dolor sit amet, consectetuer adipiscing elit, sed diam nonummy nibh euismod tincidunt ut laoreet</div>
  <div class="hr abs" style="left:602px;top:689px;width:207px"></div>
  <div class="newsimg abs" style="left:602px;top:698px" role="img" aria-label="Photo d'actualité : étudiante au travail"></div>
  <div class="newstext abs" style="left:657px;top:697px">Lorem ipsum dolor sit amet, consectetuer adipiscing elit, sed diam nonummy nibh euismod tincidunt ut laoreet</div>
  <div class="hr abs" style="left:602px;top:751px;width:207px"></div>
  <div class="newsimg abs" style="left:602px;top:760px" role="img" aria-label="Photo d'actualité : étudiante au travail"></div>
  <div class="newstext abs" style="left:657px;top:759px">Lorem ipsum dolor sit amet, consectetuer adipiscing elit, sed diam nonummy nibh euismod tincidunt ut laoreet</div>
  <div class="hr abs" style="left:602px;top:813px;width:207px"></div>
  <div class="newsimg abs" style="left:602px;top:822px" role="img" aria-label="Photo d'actualité : étudiante au travail"></div>
  <div class="newstext abs" style="left:657px;top:821px">Lorem ipsum dolor sit amet, consectetuer adipiscing elit, sed diam nonummy nibh euismod tincidunt ut laoreet</div>
  <div class="more abs" style="left:604px;top:885px">+ de nouvelles <b>&gt;&gt;</b></div>
  <div class="abs" style="left:602px;top:900px;width:207px;height:3px;background:#e0e0e0"></div>

  <div class="partners-line abs"></div>
  <svg class="abs" style="left:778px;top:916px" width="34" height="12" viewBox="0 0 34 12">
    <path d="M8 1L3 6l5 5" fill="none" stroke="#c4161c" stroke-width="2.5"/>
    <path d="M26 1l5 5-5 5" fill="none" stroke="#c4161c" stroke-width="2.5"/>
  </svg>
  <div class="partner abs" style="left:218px">Corvane</div>
  <div class="partner abs" style="left:320px">Delmira</div>
  <div class="partner abs" style="left:440px">Hexlane</div>
  <div class="partner abs" style="left:578px">Orbitra</div>
  <div class="partner abs" style="left:726px">Quillmor</div>

  <div class="abs" style="left:168px;top:996px;width:10px;height:10px;border-radius:50%;background:var(--red)"></div>
  <div class="abs" style="left:194px;top:998px;width:615px;height:6px;border-top:1px solid var(--line);border-bottom:3px solid #e5e5e5"></div>

  <footer class="footer abs">
    <div class="fcol abs" style="left:138px">
      <h4>Suivez - nous &gt;&gt;</h4>
      <ul class="social">
        <li><i></i>Friendspace</li><li><i></i>Chirply</li><li><i></i>ProNetwork</li><li><i></i>ViewStream</li>
      </ul>
    </div>
    <div class="fcol abs" style="left:271px">
      <h4>A propos</h4>
      <ul><li>A propos de l'IZPM</li><li>Admissions</li><li>Calendrier de l'ecole</li><li>Offres d'emploi</li><li>Repertoire du personnel</li></ul>
    </div>
    <div class="fcol abs" style="left:400px">
      <h4>Etudiants</h4>
      <ul><li>Accueil - Etudiants</li><li>Programmes et Formations</li><li>Vie etudiante</li><li>Entreprises</li><li>Blogue</li></ul>
    </div>
    <div class="fcol abs" style="left:541px;width:135px">
      <h4>IZPM</h4>
      <p>12, RUE DES ACACIAS<br>Quartier Belvedere, Pres du Marche des Tisserands</p>
      <p style="margin-top:12px;display:flex;gap:6px;align-items:center"><svg width="12" height="12" viewBox="0 0 24 24"><path fill="#fff" d="M6.6 10.8a15 15 0 0 0 6.6 6.6l2.2-2.2c.3-.3.7-.4 1-.2 1.1.4 2.3.6 3.6.6.6 0 1 .4 1 1V20c0 .6-.4 1-1 1A17 17 0 0 1 3 4c0-.6.4-1 1-1h3.5c.6 0 1 .4 1 1 0 1.3.2 2.5.6 3.6.1.3 0 .7-.2 1z"/></svg>(221) 33 412 77 90</p>
      <p style="margin-top:12px;display:flex;gap:6px;align-items:center"><svg width="12" height="12" viewBox="0 0 24 24"><path fill="#fff" d="M6.6 10.8a15 15 0 0 0 6.6 6.6l2.2-2.2c.3-.3.7-.4 1-.2 1.1.4 2.3.6 3.6.6.6 0 1 .4 1 1V20c0 .6-.4 1-1 1A17 17 0 0 1 3 4c0-.6.4-1 1-1h3.5c.6 0 1 .4 1 1 0 1.3.2 2.5.6 3.6.1.3 0 .7-.2 1z"/></svg>(221) 77 530 18 46</p>
    </div>
    <div class="fcol abs" style="left:699px;width:112px">
      <h4>Infolettre</h4>
      <p>Recevez les dernieres nouvelles de l'IZPM, ainsi Que des ressources utiles sur le management de projets.</p>
      <div class="news-in"><span></span><b>ENVOYER</b></div>
    </div>
    <div class="dotted abs" style="left:138px;top:141px;width:671px;border-color:rgba(255,255,255,.4)"></div>
    <div class="copy abs">© IZPM, 2014 Tous droits reserves.</div>
  </footer>

  <aside class="sidebar abs" aria-label="Réseaux sociaux"><i></i><i></i><i></i><i></i><i></i></aside>

</div>
</body>
</html>
```